Design an Elegant Handbag Brand website

I need a webiste design are looking for ideas for a new theme, color scheme, etc. You come up with the general look and feel of the home page and our team will take it from there.
We're only looking for a one (1) page layout which should be fashionable and graphic intensive, but also include the standard homepage links (about us, see our collections, etc)

Target Market(s)

Our customers are fashionable women looking for an animal friendly and environmentally friendly handbag.

Industry/Entity Type

Business

Number of Pages Required

1 page

Font styles to use
Serif
Sans Serif

Requirements
Must have
• Feel free to modify it with different colors or tweaks as you see fit. We are open to all suggestions.
Nice to have

```html
<!DOCTYPE html>
<html lang="en">
<head>
<meta charset="utf-8">
<title>Solenne Handbags</title>
<link href="https://fonts.googleapis.com/css2?family=Josefin+Sans:wght@300;400;600;700&display=swap" rel="stylesheet">
<style>
:root{
  --ink:#2d2d2d;
  --muted:#6b6b6b;
  --header:#ededed;
  --line:#e2e2e2;
  --white:#ffffff;
  --accent:#b58a6a;
}
*{box-sizing:border-box;margin:0;padding:0}
html,body{width:1200px;height:3403px;overflow:hidden;background:var(--white)}
body{position:relative;font-family:'Josefin Sans',sans-serif;color:var(--ink)}
.abs{position:absolute}
.site-header{left:0;top:0;width:1200px;height:159px;background:var(--header)}
.brand{left:172px;top:50px;display:flex;align-items:center;gap:12px;font-size:34px;font-weight:400;color:var(--ink)}
.brand-mark{width:26px;height:26px;border:2px solid var(--ink)}
.socials{left:857px;top:50px;display:flex;gap:12px}
.socials span{width:34px;height:34px;border:1.5px solid var(--ink);border-radius:50%}
.nav{top:134px;font-size:11px;letter-spacing:3.5px;font-weight:600}
.hero{left:0;top:159px;width:1200px;height:438px;
  background:
    radial-gradient(ellipse 300px 260px at 880px 200px,#e3b3b0 0%,rgba(227,179,176,.7) 45%,rgba(227,179,176,0) 100%),
    radial-gradient(ellipse 380px 300px at 230px 300px,#6a4a50 0%,rgba(106,74,80,0) 100%),
    linear-gradient(100deg,#2e2427 0%,#5a4550 28%,#5c6f9a 52%,#7b8cb6 68%,#3f4f78 100%)}
.hero-shade{left:0;top:159px;width:1200px;height:438px;background:rgba(20,16,20,.18)}
.hero-text{left:0;top:270px;width:1200px;text-align:center;color:var(--white)}
.hero-text .eyebrow{font-size:16px;letter-spacing:1px}
.hero-text h1{font-size:42px;font-weight:700;margin-top:26px;letter-spacing:.5px}
.hero-text p{font-size:14px;line-height:22px;width:410px;margin:38px auto 0;font-weight:300}
.hero-text .more{margin-top:54px;font-size:7px;letter-spacing:2px;font-weight:700}
.hero-text .more::after{content:"";display:inline-block;width:24px;height:1px;background:var(--white);margin-left:8px;vertical-align:middle}
.section-title{left:0;width:1200px;text-align:center;font-size:17px;letter-spacing:3px;font-weight:600}
.card{top:714px;width:282px;height:358px;border:1px solid var(--line)}
.card .ph{left:20px;top:40px;width:240px;height:210px}
.card .label{left:0;top:318px;width:100%;text-align:center;font-size:17px;letter-spacing:2.5px;font-weight:600}
.tile .tag{background:var(--white);padding:8px 14px 6px;font-size:22px;font-weight:300}
.tile .tag small{font-size:11px;letter-spacing:1.5px;color:var(--muted);margin-left:4px}
.seller{top:1967px;width:281px;height:392px}
.seller-name{top:2400px;width:281px;text-align:center;font-size:18px;letter-spacing:2px;font-weight:300}
.seller-price{top:2428px;width:281px;text-align:center;font-size:10px;letter-spacing:1.5px}
.promo{left:170px;top:2507px;width:858px;height:321px;background:linear-gradient(180deg,#0d0b0c 0%,#1a0b0c 60%,#4a0c0e 100%)}
.promo-photo{left:170px;top:2507px;width:330px;height:321px;
  background:radial-gradient(ellipse 130px 100px at 170px 130px,#c8202c 0%,#8e1a22 55%,rgba(40,20,22,0) 100%),linear-gradient(160deg,#1c1416,#3a1a1e 55%,#2a1214)}
.promo-text{left:500px;top:2614px;width:488px;text-align:center;color:var(--white)}
.promo-text .tag{font-size:7px;letter-spacing:2px;font-weight:700}
.promo-text h2{font-size:36px;letter-spacing:4px;font-weight:400;margin-top:18px}
.promo-text .btn{display:inline-block;margin-top:26px;border:1px solid var(--white);padding:7px 18px 5px;font-size:7px;letter-spacing:2px;font-weight:700}
.insta{top:2939px;height:218px}
.insta-label{left:478px;top:3036px;width:244px;height:24px;background:var(--white);text-align:center;font-size:7px;letter-spacing:1.5px;font-weight:700;line-height:26px}
.footer-name{left:0;top:3213px;width:1200px;text-align:center;font-size:12px;color:var(--muted)}
.footer-rule{left:157px;top:3243px;width:886px;height:1px;background:var(--line)}
.foot-key{font-size:6px;letter-spacing:1.5px;color:var(--accent);font-weight:700}
.foot-val{font-size:11px;color:var(--muted);margin-top:8px}
.foot-brand{left:0;top:3296px;width:1200px;display:flex;justify-content:center;align-items:center;gap:10px;font-size:26px}
.foot-brand .brand-mark{width:20px;height:20px}
</style>
</head>
<body>
<header class="abs site-header">
  <div class="abs brand"><span class="brand-mark"></span>Solenne Handbags</div>
  <div class="abs socials"><span></span><span></span><span></span><span></span></div>
  <div class="abs nav" style="left:172px">HOME</div>
  <div class="abs nav" style="left:260px">ABOUT</div>
  <div class="abs nav" style="left:356px">COLLECTIONS</div>
  <div class="abs nav" style="left:505px">BLOG</div>
  <div class="abs nav" style="left:591px">CONTACT</div>
</header>

<section class="abs hero" role="img" aria-label="Woman in a blue dress carrying a pink leather handbag"></section>
<div class="abs hero-shade"></div>
<div class="abs hero-text">
  <div class="eyebrow">ELEGANT</div>
  <h1>BAG FASHION BRAND</h1>
  <p>Lorem Ipsum is simply dummy text of the printing and typesetting industry. Lorem Ipsum has been the</p>
  <div class="more">SEE MORE</div>
</div>

<h2 class="abs section-title" style="top:660px">OUR TOP COLLECTIONS</h2>
<div class="abs card" style="left:172px">
  <div class="abs ph" role="img" aria-label="Beige handbag set" style="background:radial-gradient(ellipse 120px 90px at 120px 115px,#b9a084 0%,#cdb89e 55%,#f3ede6 100%)"></div>
  <div class="abs label">HANDBAGS</div>
</div>
<div class="abs card" style="left:459px">
  <div class="abs ph" role="img" aria-label="Black tote evening bag" style="background:radial-gradient(ellipse 90px 85px at 120px 120px,#151515 0%,#2a2a2a 55%,#eeeeee 100%)"></div>
  <div class="abs label" style="top:305px">EVENING BAGS</div>
</div>
<div class="abs card" style="left:745px">
  <div class="abs ph" role="img" aria-label="Pink shoulder bag" style="background:radial-gradient(ellipse 90px 85px at 120px 120px,#eea7a3 0%,#f2b8b3 55%,#fbeeed 100%)"></div>
  <div class="abs label" style="top:315px">SHOULDER BAGS</div>
</div>

<h2 class="abs section-title" style="top:1140px">DISCOVER THE COLLECTIONS</h2>
<div class="abs tile" role="img" aria-label="Woman in red sweater with a red handbag on a city street" style="left:172px;top:1199px;width:423px;height:631px;background:radial-gradient(ellipse 170px 220px at 260px 300px,#8a2438 0%,rgba(138,36,56,0) 100%),linear-gradient(160deg,#c4a88e,#9a7662 40%,#6e3a40 70%,#3e302c)">
  <div class="abs tag" style="left:72px;top:538px">Bag<small>25 Items</small></div>
</div>
<div class="abs tile" role="img" aria-label="Black and cream handbags on a table" style="left:601px;top:1199px;width:423px;height:310px;background:radial-gradient(ellipse 120px 110px at 300px 190px,#efe4d2 0%,rgba(239,228,210,0) 100%),linear-gradient(100deg,#2a201c,#5a4234 45%,#a88870)">
  <div class="abs tag" style="left:38px;top:212px">Bag<small>25 Items</small></div>
</div>
<div class="abs tile" role="img" aria-label="Hands holding a pink leather bag" style="left:601px;top:1516px;width:423px;height:314px;background:radial-gradient(ellipse 160px 120px at 180px 180px,#dba6ae 0%,rgba(219,166,174,0) 100%),linear-gradient(120deg,#c48f98,#e5bcc2 60%,#9fb6d4)">
  <div class="abs tag" style="left:40px;top:220px">Bag<small>25 Items</small></div>
</div>

<h2 class="abs section-title" style="top:1907px">OUR BEST SELLERS</h2>
<div class="abs seller" role="img" aria-label="Woman in yellow coat with black bag" style="left:172px;background:linear-gradient(90deg,rgba(0,0,0,0) 60%,rgba(20,20,20,.55)),linear-gradient(#cfcac1,#d9b92e 40%,#c8a82a 70%,#1c1c1c)"></div>
<div class="abs seller" role="img" aria-label="Woman in green coat with tan bag" style="left:459px;background:radial-gradient(ellipse 60px 50px at 150px 300px,#9a6a3e 0%,rgba(154,106,62,0) 100%),linear-gradient(#4e4238,#2c6440 50%,#1f4a30)"></div>
<div class="abs seller" role="img" aria-label="Woman in yellow top with white bag" style="left:745px;background:radial-gradient(ellipse 70px 55px at 150px 310px,#e9e4da 0%,rgba(233,228,218,0) 100%),linear-gradient(#b9a888,#e4df3a 40%,#6a6258 80%)"></div>
<div class="abs seller-name" style="left:172px">Bag Name</div>
<div class="abs seller-price" style="left:172px">Rs 10,000.00</div>
<div class="abs seller-name" style="left:459px">Bag Name</div>
<div class="abs seller-price" style="left:459px">Rs 10,000.00</div>
<div class="abs seller-name" style="left:745px">Bag Name</div>
<div class="abs seller-price" style="left:745px">Rs 10,000.00</div>

<section class="abs promo"></section>
<div class="abs promo-photo" role="img" aria-label="Woman holding a red quilted patent handbag"></div>
<div class="abs promo-text">
  <div class="tag">#NEW COLLECTION 2020</div>
  <h2>NEW HANDBAGS</h2>
  <div class="btn">SHOP NOW</div>
</div>

<h2 class="abs section-title" style="top:2896px">FOLLOW US</h2>
<div class="abs insta" role="img" aria-label="Woman with white bag" style="left:165px;width:145px;background:linear-gradient(#5a5048,#d8d03a 45%,#bdb5a8)"></div>
<div class="abs insta" role="img" aria-label="Pink bag close-up" style="left:310px;width:145px;background:linear-gradient(135deg,#b88890,#e3bfc4)"></div>
<div class="abs insta" role="img" aria-label="Woman with red bag" style="left:455px;width:145px;background:linear-gradient(#b89a84,#8a2a3c 60%,#4a2e2c)"></div>
<div class="abs insta" role="img" aria-label="Pink bag with blue dress" style="left:600px;width:145px;background:linear-gradient(135deg,#5d6f9c,#d8a9a6)"></div>
<div class="abs insta" role="img" aria-label="Woman in yellow coat" style="left:745px;width:145px;background:linear-gradient(#cfcac1,#d9b92e 45%,#1c1c1c)"></div>
<div class="abs insta" role="img" aria-label="Woman in green coat" style="left:890px;width:142px;background:linear-gradient(#4e4238,#2c6440 55%,#8a5a35)"></div>
<div class="abs insta-label">INSTAGRAM @SOLENNE_HANDBAGS.STUDIO</div>

<div class="abs footer-name">Solenne Handbags</div>
<div class="abs footer-rule"></div>
<div class="abs" style="left:172px;top:3298px">
  <div class="foot-key">ADDRESS</div>
  <div class="foot-val">Lorem sit amet, consectetur</div>
</div>
<div class="abs foot-brand"><span class="brand-mark"></span>Solenne Handbags</div>
<div class="abs" style="left:880px;top:3298px;width:144px;text-align:right">
  <div class="foot-key">PHONE</div>
  <div class="foot-val">00 (555) 210 48 36</div>
</div>
</body>
</html>
```